No Trespassing Jobsite Sign for Construction Company

This Poster is for a 24"X18" 'NO TRESPASSING' job site sign for a construction company.

- please include ALL verbiage as indicated in the 'MOCKUP' attachment
- please include two (2) design options; one with each of the uploaded logos
- we would like to follow the same design as our 'Job Site Safety' which I have also uploaded
- this poster must look professional and sleek

if you have any questions, please send me a message

```html
<!DOCTYPE html>
<html lang="en">
<head>
<meta charset="utf-8">
<title>No Trespassing Jobsite Sign – Two Options</title>
<link href="https://fonts.googleapis.com/css2?family=Montserrat:wght@500;700;800;900&family=Oswald:wght@400;500;600&family=Libre+Baskerville:wght@400;700&display=swap" rel="stylesheet">
<style>
  :root {
    --board: #6a9a58;
    --paper: #fbfbfa;
    --red: #e4202a;
    --red-deep: #c8161f;
    --yellow: #f7c41a;
    --black: #141414;
    --navy: #1f2f7a;
    --ink: #2a2a2a;
    --grey: #8a8a8a;
  }
  * { box-sizing: border-box; margin: 0; padding: 0; }
  html, body { width: 917px; height: 1200px; overflow: hidden; }
  body { background: var(--board); position: relative; }

  .sign {
    position: absolute; left: 88px; width: 740px; height: 555px;
    background: var(--paper);
    overflow: hidden;
    box-shadow: 0 2px 8px rgba(0,0,0,.18);
  }
  .sign--option-one { top: 30px; }
  .sign--option-two { top: 615px; }

  .hazard-edge {
    position: absolute; left: 0; width: 100%; height: 13px;
    background: repeating-linear-gradient(-60deg, var(--yellow) 0 28px, var(--black) 28px 56px);
  }
  .hazard-edge--top { top: 0; }
  .hazard-edge--bottom { bottom: 0; }

  .hazard-band {
    position: absolute; left: 0; top: 245px; width: 100%; height: 180px;
    background: repeating-linear-gradient(-50deg, var(--yellow) 0 70px, var(--black) 70px 140px);
  }

  .warning-icon { position: absolute; left: 22px; top: 32px; width: 82px; height: 74px; }
  .stop-badge { position: absolute; right: 22px; top: 30px; width: 78px; height: 78px; }

  .headline {
    position: absolute; left: 0; right: 0; top: 40px; text-align: center;
    font-family: "Montserrat", sans-serif; font-weight: 900; font-size: 45px;
    color: var(--red); letter-spacing: .5px; line-height: 1;
  }
  .headline-rule {
    position: absolute; left: 160px; width: 420px; top: 96px; height: 1px; background: var(--ink);
  }
  .headline-rule::after {
    content: ""; position: absolute; left: 200px; top: -3px; width: 20px; height: 6px;
    border: 1px solid var(--ink); border-radius: 50%; background: var(--paper);
  }
  .warning-copy {
    position: absolute; left: 0; right: 0; top: 108px; text-align: center;
    font-family: "Montserrat", sans-serif; font-weight: 500; font-size: 15px;
    color: var(--red); line-height: 20px;
  }
  .warning-copy strong { font-weight: 800; }

  .safety-cards { position: absolute; left: 117px; top: 196px; width: 500px; height: 252px; display: flex; }
  .card {
    width: 125px; height: 100%; position: relative; text-align: center; overflow: hidden;
    font-family: "Oswald", sans-serif; border-radius: 3px;
  }
  .card--light { background: linear-gradient(90deg, #b9b9b9, #f7f7f7 18%, #ffffff 60%, #d8d8d8); }
  .card__head {
    height: 58px; padding-top: 10px; color: #fff; font-size: 14.5px; line-height: 17px; font-weight: 500;
  }
  .card__head--red { background: linear-gradient(90deg, var(--red-deep), var(--red) 30%, var(--red) 80%, #b5141c); }
  .card__title { padding-top: 10px; font-size: 15px; font-weight: 500; line-height: 17px; }
  .card__title--dark { color: var(--ink); }
  .card__title--red { color: var(--red); }
  .card__sub { font-family: "Oswald", sans-serif; font-weight: 400; font-size: 8px; line-height: 9.5px; display: block; }
  .card__visual { display: block; width: 100%; }
  .card__foot {
    position: absolute; left: 0; bottom: 0; width: 100%; color: #fff;
    font-size: 9.5px; line-height: 11.5px; font-weight: 500; padding: 0 10px;
    display: flex; align-items: center; justify-content: center;
  }
  .card__foot--red { background: linear-gradient(90deg, var(--red-deep), var(--red) 30%, var(--red) 80%, #b5141c); }
  .card__text { font-size: 8.5px; line-height: 10.5px; color: var(--ink); font-weight: 500; padding: 0 10px; }

  .ppe-list { list-style: none; text-align: left; padding-left: 16px; margin-top: 6px; }
  .ppe-list li {
    font-size: 7.5px; line-height: 13px; font-weight: 500; color: var(--ink); text-transform: uppercase; position: relative;
  }
  .ppe-list li::before {
    content: ""; position: absolute; left: -8px; top: 5px; width: 3.5px; height: 3.5px; border-radius: 50%; background: var(--red);
  }

  .brand {
    position: absolute; left: 0; right: 0; display: flex; justify-content: center; align-items: center;
    font-family: "Libre Baskerville", serif; color: var(--navy);
  }
  .brand__name { font-size: 20px; font-weight: 700; line-height: 1; }
  .brand__divider { width: 1px; height: 34px; background: var(--navy); margin: 0 12px; }
  .brand__tag { font-size: 15px; font-weight: 700; line-height: 16px; text-align: center; }
  .sign--option-one .brand { top: 468px; }
  .sign--option-two .brand { top: 462px; }
  .sign--option-two .brand__name { font-size: 24px; }
  .sign--option-two .brand__tag { font-size: 18px; line-height: 19px; }

  .web-address {
    position: absolute; left: 0; right: 0; top: 508px; text-align: center;
    font-family: "Libre Baskerville", serif; font-weight: 700; font-size: 24px; color: var(--navy);
  }
  .slogan {
    position: absolute; left: 120px; width: 440px; top: 514px; text-align: center;
    font-family: "Libre Baskerville", serif; font-size: 19px; color: var(--navy);
  }
  .web-address--small {
    position: absolute; right: 24px; top: 506px; font-family: "Libre Baskerville", serif;
    font-size: 11px; font-weight: 700; color: var(--navy);
  }
  .license {
    position: absolute; right: 24px; top: 522px;
    font-family: "Libre Baskerville", serif; font-size: 10px; color: var(--navy);
  }
  .sign--option-one .license { top: 520px; }
</style>
</head>
<body>

<!-- Option one: compact company name with web address -->
<section class="sign sign--option-one" aria-label="No trespassing sign, option one">
  <div class="hazard-edge hazard-edge--top"></div>
  <div class="hazard-band"></div>

  <svg class="warning-icon" viewBox="0 0 82 74" aria-hidden="true">
    <path d="M41 5 L78 69 L4 69 Z" fill="#f7e017" stroke="#141414" stroke-width="6" stroke-linejoin="round"/>
    <rect x="37" y="24" width="8" height="27" rx="4" fill="#141414"/>
    <circle cx="41" cy="59" r="4.5" fill="#141414"/>
  </svg>
  <svg class="stop-badge" viewBox="0 0 78 78" role="img" aria-label="Red stop octagon with raised hand">
    <polygon points="23,2 55,2 76,23 76,55 55,76 23,76 2,55 2,23" fill="#e4202a" stroke="#ffffff" stroke-width="3"/>
  </svg>

  <h1 class="headline">NO TRESPASSING</h1>
  <div class="headline-rule"></div>
  <p class="warning-copy">THIS IS DESIGNATED CONTRUCTION SITE. ANYONE<br>TRESPASSING ON THIS PROPERTY, UPON CONVICTION,<br><strong>SHALL BE GUILTY OF A FELONY.</strong></p>

  <div class="safety-cards">
    <div class="card">
      <div class="card__head card__head--red">CONSTRUCTION<br>WORK IN PROGRESS</div>
      <svg class="card__visual" width="125" height="112" role="img" aria-label="Hard hat over an under construction diamond sign on hazard stripes"><defs><linearGradient id="g1a" x1="0" y1="0" x2="1" y2="1"><stop offset="0" stop-color="#f4b400"/><stop offset="1" stop-color="#3a3a3a"/></linearGradient></defs><rect width="125" height="112" fill="url(#g1a)"/></svg>
      <div class="card__foot card__foot--red" style="height:82px">Unauthorized<br>Entry to this site is<br>strictly prohibited</div>
    </div>
    <div class="card card--light">
      <div class="card__title card__title--dark">P.P.E.ITEMS<span class="card__sub">P.P.E. Items Must be worn as<br>required by OSHA standards<br>and Jobsite Safety requirements</span></div>
      <svg class="card__visual" width="125" height="88" role="img" aria-label="Safety gear: helmet, gloves, goggles and harness"><defs><linearGradient id="g1b"><stop offset="0" stop-color="#e08a2c"/><stop offset=".5" stop-color="#f2f2f2"/><stop offset="1" stop-color="#e2b42a"/></linearGradient></defs><rect width="125" height="88" fill="url(#g1b)"/></svg>
      <ul class="ppe-list"><li>Safety helments</li><li>Eye protection</li><li>Fall protection</li><li>Hearing protection</li><li>High visibility clothing</li><li>Protective footwear</li></ul>
    </div>
    <div class="card card--light">
      <div class="card__title card__title--red">FIRST AID KIT<span class="card__sub" style="color:#2a2a2a">Available<br>onsite</span></div>
      <svg class="card__visual" width="125" height="92" role="img" aria-label="Open red first aid kit with supplies"><defs><linearGradient id="g1c" x1="0" y1="0" x2="0" y2="1"><stop offset="0" stop-color="#d9232b"/><stop offset="1" stop-color="#e9e9e9"/></linearGradient></defs><rect width="125" height="92" fill="url(#g1c)"/></svg>
      <p class="card__text" style="margin-top:8px;font-weight:600">If first aid supplies are needed, please see superintendent to access the first aid kit available onsite. Call 911 in case of emergency</p>
    </div>
    <div class="card">
      <div class="card__head card__head--red" style="height:62px">NO SMOKING<span class="card__sub">Smoking prohibited<br>on site</span></div>
      <svg class="card__visual" width="125" height="92" role="img" aria-label="No smoking symbol over a cigarette"><rect width="125" height="92" fill="#f3f3f3"/></svg>
      <div class="card__foot card__foot--red" style="height:98px">Smoking is designated areas only. Period. In Case of emergency, Fire Extinguisher is located onsite</div>
    </div>
  </div>

  <div class="brand">
    <span class="brand__name">Harlow &amp; Company, Inc.</span>
    <span class="brand__divider"></span>
    <span class="brand__tag">General<br>Contractors</span>
  </div>
  <p class="web-address">www.harlowbuilders.net</p>
  <p class="license">CGC4827105</p>
  <div class="hazard-edge hazard-edge--bottom"></div>
</section>

<!-- Option two: larger company name with slogan -->
<section class="sign sign--option-two" aria-label="No trespassing sign, option two">
  <div class="hazard-edge hazard-edge--top"></div>
  <div class="hazard-band"></div>

  <svg class="warning-icon" viewBox="0 0 82 74" aria-hidden="true">
    <path d="M41 5 L78 69 L4 69 Z" fill="#f7e017" stroke="#141414" stroke-width="6" stroke-linejoin="round"/>
    <rect x="37" y="24" width="8" height="27" rx="4" fill="#141414"/>
    <circle cx="41" cy="59" r="4.5" fill="#141414"/>
  </svg>
  <svg class="stop-badge" viewBox="0 0 78 78" role="img" aria-label="Red stop octagon with raised hand">
    <polygon points="23,2 55,2 76,23 76,55 55,76 23,76 2,55 2,23" fill="#e4202a" stroke="#ffffff" stroke-width="3"/>
  </svg>

  <h1 class="headline">NO TRESPASSING</h1>
  <div class="headline-rule"></div>
  <p class="warning-copy">THIS IS DESIGNATED CONTRUCTION SITE. ANYONE<br>TRESPASSING ON THIS PROPERTY, UPON CONVICTION,<br><strong>SHALL BE GUILTY OF A FELONY.</strong></p>

  <div class="safety-cards">
    <div class="card">
      <div class="card__head card__head--red">CONSTRUCTION<br>WORK IN PROGRESS</div>
      <svg class="card__visual" width="125" height="112" role="img" aria-label="Hard hat over an under construction diamond sign on hazard stripes"><defs><linearGradient id="g2a" x1="0" y1="0" x2="1" y2="1"><stop offset="0" stop-color="#f4b400"/><stop offset="1" stop-color="#3a3a3a"/></linearGradient></defs><rect width="125" height="112" fill="url(#g2a)"/></svg>
      <div class="card__foot card__foot--red" style="height:82px">Unauthorized<br>Entry to this site is<br>strictly prohibited</div>
    </div>
    <div class="card card--light">
      <div class="card__title card__title--dark">P.P.E.ITEMS<span class="card__sub">P.P.E. Items Must be worn as<br>required by OSHA standards<br>and Jobsite Safety requirements</span></div>
      <svg class="card__visual" width="125" height="88" role="img" aria-label="Safety gear: helmet, gloves, goggles and harness"><defs><linearGradient id="g2b"><stop offset="0" stop-color="#e08a2c"/><stop offset=".5" stop-color="#f2f2f2"/><stop offset="1" stop-color="#e2b42a"/></linearGradient></defs><rect width="125" height="88" fill="url(#g2b)"/></svg>
      <ul class="ppe-list"><li>Safety helments</li><li>Eye protection</li><li>Fall protection</li><li>Hearing protection</li><li>High visibility clothing</li><li>Protective footwear</li></ul>
    </div>
    <div class="card card--light">
      <div class="card__title card__title--red">FIRST AID KIT<span class="card__sub" style="color:#2a2a2a">Available<br>onsite</span></div>
      <svg class="card__visual" width="125" height="92" role="img" aria-label="Open red first aid kit with supplies"><defs><linearGradient id="g2c" x1="0" y1="0" x2="0" y2="1"><stop offset="0" stop-color="#d9232b"/><stop offset="1" stop-color="#e9e9e9"/></linearGradient></defs><rect width="125" height="92" fill="url(#g2c)"/></svg>
      <p class="card__text" style="margin-top:8px;font-weight:600">If first aid supplies are needed, please see superintendent to access the first aid kit available onsite. Call 911 in case of emergency</p>
    </div>
    <div class="card">
      <div class="card__head card__head--red" style="height:62px">NO SMOKING<span class="card__sub">Smoking prohibited<br>on site</span></div>
      <svg class="card__visual" width="125" height="92" role="img" aria-label="No smoking symbol over a cigarette"><rect width="125" height="92" fill="#f3f3f3"/></svg>
      <div class="card__foot card__foot--red" style="height:98px">Smoking is designated areas only. Period. In Case of emergency, Fire Extinguisher is located onsite</div>
    </div>
  </div>

  <div class="brand">
    <span class="brand__name">Harlow &amp; Company, Inc.</span>
    <span class="brand__divider"></span>
    <span class="brand__tag">General<br>Contractors</span>
  </div>
  <p class="slogan">“Building Trust on Every Site”</p>
  <p class="web-address--small">www.harlowbuilders.net</p>
  <p class="license">CGC4827105</p>
  <div class="hazard-edge hazard-edge--bottom"></div>
</section>

</body>
</html>
```